I want to create a postcard we can use as a promotional offer. We may send out to prospects or give to people at an event to get them in front of us and start to understand their business more with the hope of engaging them as clients eventually.
The offer is a Complimentary "Pathwise Launch Pack". (valued at $875)
The kit includes:
Finance Prism Review
45 minute Business Discovery Meeting
6 point Diagnostic Report
3 Recommendations for your Business

The headline and there look and feel we would like the design to be focused upon is "Analyze. Boost. Grow."
Include an Image(s) as you feel appropriate.
I'm thinking Headline/Mian Branding and Picture on the Front, then Offer and details of Kit and Logos etc on the Back.

Include 2 logos as we are part of a joint operation, Meridel Accountants & Trovandel.

Call to action to Phone 0255501842 or email hello@trovandel.example.com.au

Logo's uploaded, committed payment, increased deadline.

Target Market(s)

Small to Medium Business

Industry/Entity Type

Business

Requirements
Must have
• Logos in Colour on Back with rest of Detail.
Front to be all about the key message "Analyze. Boost. Grow." select pic to represent.
Must create cut through and intrigue to make the holder tunr the card and read.

```html
<!DOCTYPE html>
<html lang="en">
<head>
<meta charset="utf-8">
<title>Pathwise Launch Pack Postcard</title>
<link rel="stylesheet" href="https://fonts.googleapis.com/css2?family=Open+Sans:ital,wght@0,400;0,600;0,700;0,800;1,600;1,700;1,800&display=swap">
<style>
  :root {
    --green: #5aad2e;
    --green-dark: #3f8f1f;
    --blue: #1f5f8b;
    --blue-deep: #174a70;
    --sky-top: #b9d6ee;
    --sky-mid: #e6f1f8;
    --meadow: #86b94a;
    --bar-light: #d6e8f5;
    --paper: #ffffff;
    --ink: #1d4f78;
  }
  * { box-sizing: border-box; margin: 0; padding: 0; }
  html, body { width: 1181px; height: 1200px; overflow: hidden; background: #ffffff; }
  body { position: relative; font-family: "Open Sans", Arial, sans-serif; color: var(--ink); }

  .card { position: absolute; background: var(--paper); overflow: hidden; box-shadow: 0 4px 14px rgba(0,0,0,.18); }
  .card--front { left: 40px; top: 34px; width: 730px; height: 570px; }
  .card--back { left: 395px; top: 592px; width: 750px; height: 580px;
    background: linear-gradient(180deg, #cfe5f4 0%, #eef6fb 45%, #ffffff 75%); }

  /* front */
  .front__photo { position: absolute; left: 0; top: 0; width: 730px; height: 430px;
    background: linear-gradient(180deg, var(--sky-top) 0%, var(--sky-mid) 52%, #cfe3c4 66%, var(--meadow) 100%); }
  .headline { position: absolute; left: 470px; top: 70px; font-weight: 800; font-style: italic;
    font-size: 52px; line-height: 62px; letter-spacing: -0.5px; }
  .headline .g { color: var(--green); display: block; }
  .headline .b { color: var(--blue); display: block; }
  .front__swoosh { position: absolute; left: 0; top: 350px; }
  .pillar { position: absolute; width: 84px; height: 84px; border-radius: 50%; border: 3px solid #fff;
    display: flex; flex-direction: column; align-items: center; justify-content: flex-end;
    padding-bottom: 14px; color: #fff; font-size: 10px; font-weight: 600; box-shadow: 0 2px 5px rgba(0,0,0,.25); }
  .pillar--blue { background: var(--blue); }
  .pillar--green { background: var(--green); }
  .pillar svg { margin-bottom: 4px; }

  .brands { position: absolute; display: flex; align-items: center; }
  .brand { display: flex; align-items: center; gap: 10px; font-weight: 800; font-size: 34px; white-space: nowrap; }
  .brand--meridel { color: var(--blue-deep); }
  .brand--trovandel { color: var(--green-dark); }
  .brand__square { width: 22px; height: 22px; background: var(--blue-deep); }
  .brand__circle { width: 24px; height: 24px; border-radius: 50%; background: var(--green); }
  .brands__divider { width: 2px; height: 64px; background: var(--blue-deep); margin: 0 32px; }

  .contact { position: absolute; height: 40px; display: flex; align-items: center; gap: 26px;
    padding-left: 20px; background: linear-gradient(90deg, var(--bar-light), #eef6fb 70%, rgba(255,255,255,0));
    border-top: 2px solid #fff; font-weight: 700; font-style: italic; color: var(--blue-deep); white-space: nowrap; }
  .contact__item { display: flex; align-items: center; gap: 10px; }

  /* back */
  .stamp { position: absolute; left: 30px; top: 30px; width: 110px; height: 110px; border-radius: 50%;
    border: 4px solid #2e7fb4; transform: rotate(-22deg); display: flex; align-items: center; justify-content: center; }
  .stamp::before { content: ""; position: absolute; inset: 7px; border-radius: 50%; border: 2px solid #2e7fb4; }
  .stamp__label { background: #2e7fb4; color: #fff; font-weight: 800; font-size: 12px; letter-spacing: .5px;
    padding: 3px 6px; width: 130px; text-align: center; position: relative; }
  .back__title { position: absolute; left: 150px; width: 600px; top: 18px; text-align: center;
    font-weight: 800; font-size: 40px; color: var(--green); letter-spacing: -0.5px; white-space: nowrap; }
  .back__tagline { position: absolute; left: 150px; width: 600px; top: 74px; text-align: center;
    font-weight: 700; font-style: italic; font-size: 17px; color: var(--green-dark); white-space: nowrap; }
  .back__copy { position: absolute; left: 170px; width: 560px; text-align: center; font-size: 13.5px;
    line-height: 19px; font-weight: 600; color: #2a7fb8; }
  .back__copy strong { color: var(--blue-deep); font-weight: 700; }
  .back__copy--one { top: 108px; }
  .back__copy--two { top: 172px; }
  .back__plant { position: absolute; left: 18px; top: 195px; width: 112px; height: 170px; border-radius: 40px 40px 10px 10px;
    background: linear-gradient(180deg, #7cbf4a 0%, #4f9b2c 68%, #b9bec2 82%, #8d9398 100%); }

  .feature { position: absolute; display: flex; align-items: center; }
  .feature__num { width: 56px; text-align: center; font-weight: 800; color: var(--green); font-size: 40px; line-height: 36px; }
  .feature__num small { display: block; font-size: 12px; line-height: 12px; color: var(--blue-deep); font-weight: 700; }
  .feature__bar { height: 24px; background: linear-gradient(180deg, #2a74a6, var(--blue-deep)); color: #fff;
    font-size: 11.5px; line-height: 16px; font-weight: 700; padding: 4px 10px; border-radius: 0 12px 12px 0;
    width: 236px; white-space: nowrap; }

  .back__band { position: absolute; left: 0; top: 350px; }
  .cta { position: absolute; left: 40px; width: 520px; text-align: center; white-space: nowrap; }
  .cta__lead { top: 410px; font-size: 15px; font-weight: 700; color: var(--green-dark); }
  .cta__lead span { color: var(--blue-deep); }
  .cta__title { top: 430px; font-size: 33px; font-weight: 800; color: var(--green); letter-spacing: -0.5px; }

  .offer { position: absolute; left: 572px; top: 360px; width: 150px; height: 150px; }
  .offer__ray { position: absolute; inset: 12px; background: var(--blue-deep); }
  .offer__ray:nth-child(2) { transform: rotate(30deg); }
  .offer__ray:nth-child(3) { transform: rotate(60deg); }
  .offer__text { position: absolute; inset: 0; display: flex; flex-direction: column; align-items: center;
    justify-content: center; color: #fff; font-weight: 800; font-size: 27px; line-height: 28px; text-align: center; }
  .offer__text small { font-size: 10px; line-height: 14px; color: #a6dd7d; font-weight: 700; margin-top: 2px; }
</style>
</head>
<body>

<section class="card card--front">
  <div class="front__photo" role="img" aria-label="Photo of open hands cupping a small bonsai tree against blue sky, lake and green meadow"></div>

  <h1 class="headline">
    <span class="g">Analyze.</span>
    <span class="b">Boost.</span>
    <span class="g">Grow.</span>
  </h1>

  <svg class="front__swoosh" width="730" height="220" viewBox="0 0 730 220" aria-hidden="true">
    <path d="M0 105 Q 360 -10 730 70 L730 220 L0 220 Z" fill="#ffffff"/>
    <path d="M0 96 Q 360 -20 730 60" fill="none" stroke="#1f5f8b" stroke-width="12"/>
    <path d="M0 112 Q 360 2 730 80" fill="none" stroke="#bcd8ee" stroke-width="4"/>
  </svg>

  <div class="pillar pillar--blue" style="left:300px; top:318px;">
    <svg width="30" height="24" viewBox="0 0 30 24"><path d="M3 12 L11 20 L27 3" fill="none" stroke="#7fd04a" stroke-width="5" stroke-linecap="round" stroke-linejoin="round"/></svg>
    Performance
  </div>
  <div class="pillar pillar--green" style="left:388px; top:300px;">Wealth</div>
  <div class="pillar pillar--blue" style="left:476px; top:306px;">Lifestyle</div>
  <div class="pillar pillar--green" style="left:564px; top:332px;">Dreams</div>

  <div class="brands" style="left:105px; top:458px;">
    <div class="brand brand--meridel"><span class="brand__square"></span>Meridel</div>
    <div class="brands__divider"></div>
    <div class="brand brand--trovandel"><span class="brand__circle"></span>Trovandel</div>
  </div>

  <div class="contact" style="left:30px; top:518px; width:680px; font-size:23px;">
    <span class="contact__item">
      <svg width="26" height="20" viewBox="0 0 26 20" aria-hidden="true"><path d="M2 6 Q13 -2 24 6 L21 9 L17 7 L17 5 Q13 3.5 9 5 L9 7 L5 9 Z M6 11 H20 L22 18 H4 Z" fill="#5aad2e"/></svg>
      0255501842
    </span>
    <span class="contact__item">
      <svg width="26" height="20" viewBox="0 0 26 20" aria-hidden="true"><rect x="1" y="2" width="24" height="16" fill="#5aad2e"/><path d="M1 2 L13 11 L25 2" fill="none" stroke="#fff" stroke-width="2"/></svg>
      hello@trovandel.example.com.au
    </span>
  </div>
</section>

<section class="card card--back">
  <div class="stamp"><span class="stamp__label">COMPLIMENTARY</span></div>

  <h2 class="back__title">Pathwise Launch Pack</h2>
  <p class="back__tagline">Bring Dreams to Life by Maximising Business Potential</p>

  <p class="back__copy back__copy--one">Between <strong>Strong Fiscal Monitoring</strong> and <strong>Support from Meridel</strong>, and <strong>Dynamic Business Development and Growth</strong> from Trovandel, we have the capabilities required to drive your business forward.</p>
  <p class="back__copy back__copy--two">Our <strong>Pathwise Launch Pack</strong> enables you to gain a snap shot of how <strong>your business</strong> is performing along with some <strong>fresh ideas</strong>, and at the same time allows you to gain insight in to how we like to look after our business clients. The rest is up to you.</p>

  <div class="back__plant" role="img" aria-label="Potted topiary plant shaped like a dollar sign"></div>

  <div class="feature" style="left:136px; top:255px;">
    <div class="feature__num">45<small>minutes</small></div>
    <div class="feature__bar">Business Discovery Meeting</div>
  </div>
  <div class="feature" style="left:440px; top:248px;">
    <div class="feature__num">6<small>point</small></div>
    <div class="feature__bar">Diagnostic Report</div>
  </div>
  <div class="feature" style="left:136px; top:318px;">
    <div class="feature__num">3</div>
    <div class="feature__bar">Recommendations for your Business</div>
  </div>
  <div class="feature" style="left:440px; top:312px;">
    <div class="feature__num">1</div>
    <div class="feature__bar">Finance Prism Review</div>
  </div>

  <svg class="back__band" width="750" height="60" viewBox="0 0 750 60" aria-hidden="true">
    <path d="M0 42 Q 300 0 610 28" fill="none" stroke="#1f5f8b" stroke-width="6"/>
  </svg>

  <p class="cta cta__lead">Take your <span>Business</span> in a <span>New Direction</span> and request your</p>
  <p class="cta cta__title">Pathwise Launch Pack</p>

  <div class="offer">
    <div class="offer__ray"></div>
    <div class="offer__ray"></div>
    <div class="offer__ray"></div>
    <div class="offer__text">FREE<br>OFFER<small>Valued At $875</small></div>
  </div>

  <div class="brands" style="left:70px; top:476px;">
    <div class="brand brand--meridel"><span class="brand__square"></span>Meridel</div>
    <div class="brands__divider"></div>
    <div class="brand brand--trovandel"><span class="brand__circle"></span>Trovandel</div>
  </div>

  <div class="contact" style="left:40px; top:536px; width:680px; font-size:19px; font-style:normal;">
    <span class="contact__item">
      <svg width="24" height="18" viewBox="0 0 26 20" aria-hidden="true"><path d="M2 6 Q13 -2 24 6 L21 9 L17 7 L17 5 Q13 3.5 9 5 L9 7 L5 9 Z M6 11 H20 L22 18 H4 Z" fill="#5aad2e"/></svg>
      0255501842
    </span>
    <span class="contact__item">
      <svg width="24" height="18" viewBox="0 0 26 20" aria-hidden="true"><rect x="1" y="2" width="24" height="16" fill="#5aad2e"/><path d="M1 2 L13 11 L25 2" fill="none" stroke="#fff" stroke-width="2"/></svg>
      hello@trovandel.example.com.au
    </span>
  </div>
</section>

</body>
</html>
```